i need a business card for a plumbing company in california

we are a drain cleaning , maintenance plumbing company who is starting new marketing campaign for a tatrench-less pipe installation department .

Target Market(s)

the professional who appreciates time and quality workmanship.

Industry/Entity Type

Plumbing

Colors
0655a3
ec1f27

Requirements
Must have
• the second logo needs to be included
Nice to have
• a focus on the services offered
Should not have
• any underlined words on the brief

```html
<!DOCTYPE html>
<html lang="en">
<head>
<meta charset="utf-8">
<title>Pipeworks Pro Plus – Business Card</title>
<link rel="stylesheet" href="https://fonts.googleapis.com/css2?family=Roboto:wght@400;500;700&display=swap">
<style>
  :root {
    --backdrop: #2b2b2d;
    --card: #050505;
    --red: #ec1f27;
    --blue: #0655a3;
    --grey: #8d8a86;
    --text: #e6e6e6;
  }
  * { margin: 0; padding: 0; box-sizing: border-box; }
  html, body { width: 1200px; height: 834px; overflow: hidden; }
  body {
    background: var(--backdrop);
    font-family: "Roboto", Arial, sans-serif;
    display: flex;
    flex-direction: column;
    align-items: center;
    justify-content: center;
    gap: 48px;
  }
  .card {
    position: relative;
    width: 640px;
    height: 366px;
    background: var(--card);
    overflow: hidden;
    box-shadow: 0 10px 30px rgba(0,0,0,.5);
  }
  .card-lines { position: absolute; inset: 0; width: 100%; height: 100%; }

  /* Front */
  .front-brand {
    position: absolute;
    left: 50%; top: 44%;
    transform: translate(-50%, -50%);
    display: flex; align-items: center; gap: 12px;
  }
  .front-brand .brand-name {
    font-weight: 700; font-size: 36px; color: var(--grey);
    letter-spacing: .5px; white-space: nowrap;
  }
  .brand-mark { width: 22px; height: 22px; background: var(--red); }
  .services-line {
    position: absolute; left: 0; right: 0; bottom: 22px;
    text-align: center;
    color: var(--red); font-size: 12.5px; letter-spacing: .3px;
    white-space: nowrap;
  }

  /* Back */
  .social-list {
    position: absolute; left: 28px; top: 26px;
    list-style: none; display: flex; flex-direction: column; gap: 8px;
  }
  .contact-item {
    display: flex; align-items: center; gap: 8px;
    color: var(--text); font-size: 12px;
  }
  .contact-icon {
    width: 12px; height: 12px; border-radius: 50%;
    background: var(--red); flex: none;
  }
  .contact-icon.is-blue { background: var(--blue); }
  .contact-icon svg { display: block; width: 12px; height: 12px; }
  .identity {
    position: absolute; left: 190px; top: 150px;
    display: flex; align-items: flex-start; gap: 26px;
  }
  .identity-brand { display: flex; align-items: center; gap: 7px; margin-top: 4px; }
  .identity-brand .brand-mark { width: 14px; height: 14px; border-radius: 50%; background: var(--blue); }
  .identity-brand .brand-name { color: var(--blue); font-weight: 700; font-size: 14px; }
  .person { text-align: right; }
  .person-name { color: var(--blue); font-size: 22px; font-weight: 500; }
  .person-rule { height: 2px; background: var(--red); margin: 6px 0 4px; }
  .person-title { color: var(--text); font-size: 13px; }
  .web-list {
    position: absolute; right: 34px; top: 248px;
    list-style: none; display: flex; flex-direction: column; gap: 7px;
  }
</style>
</head>
<body>

  <section class="card card-front" aria-label="Card front">
    <svg class="card-lines" viewBox="0 0 640 366" aria-hidden="true">
      <polygon points="0,300 0,366 28,366" fill="var(--red)"/>
      <polygon points="612,366 640,330 640,366" fill="var(--red)"/>
    </svg>
    <div class="front-brand">
      <span class="brand-name">Pipeworks Pro Plus</span>
      <span class="brand-mark"></span>
    </div>
    <p class="services-line">Trench-Less Sewer Installs &amp; Replacements – Pipe Bursting &amp; Pipe Piercing Install, Replacement Pipe</p>
  </section>

  <section class="card card-back" aria-label="Card back">
    <svg class="card-lines" viewBox="0 0 640 366" aria-hidden="true">
      <line x1="0" y1="118" x2="640" y2="118" stroke="var(--red)" stroke-width="3"/>
      <polygon points="440,0 640,0 640,20 460,20" fill="var(--red)"/>
      <line x1="0" y1="330" x2="640" y2="330" stroke="var(--red)" stroke-width="3"/>
    </svg>

    <ul class="social-list">
      <li class="contact-item"><span class="contact-icon is-blue"></span>Facebook@PipeworksPro</li>
      <li class="contact-item"><span class="contact-icon"></span>PipeworksProPlus</li>
      <li class="contact-item">
        <span class="contact-icon">
          <svg viewBox="0 0 12 12"><path d="M4 3 L5 5 L4.3 5.7 Q5 7 6.3 7.7 L7 7 L9 8 L8.5 9.3 Q5 9.5 2.7 5 Q2.5 3.5 4 3Z" fill="#fff"/></svg>
        </span>Phone: 2095550147
      </li>
    </ul>

    <div class="identity">
      <div class="identity-brand">
        <span class="brand-mark"></span>
        <span class="brand-name">Pipeworks Pro Plus</span>
      </div>
      <div class="person">
        <p class="person-name">Marco Delgado Jr</p>
        <div class="person-rule"></div>
        <p class="person-title">Owner</p>
      </div>
    </div>

    <ul class="web-list">
      <li class="contact-item"><span class="contact-icon"></span>www.PipeworksProPlus.com</li>
      <li class="contact-item"><span class="contact-icon"></span>info@PipeworksProPlus.com</li>
    </ul>
  </section>

</body>
</html>
```